Packaging design for handmade soap

We are looking for a packaging design for a brand new product line: handmade soaps, called QELVA

We are looking for a design of an outer box together with the logo. We need the design for a 90x65x30mm box (see attached). We trying to get a high-end product preferable with vintage elements (but we don't want a shiny box, it will be finished with matte lacque, however logo or other certain elements could be shiny).

The design should reflect the fact that we have a handmade, all natural soap.

I uploaded a couple of packaging examples I like.

UPDATE 1: It also should have a title, which describes the product more accurate, like "Natural Soap with Seabuckthorn and Olive oil"

UPDATE 2: I would remove the expression "high-end" from the description if high end would mean a lot of flowers in the background. I would like if you would insist about the ideea of "natural" in your works

UPDATE 3: Prefered colors green and brown (which brings the ideea of nature, natural)

Target Market(s)

Women 20-45 years with above average income

Industry/Entity Type

Cosmetics

Font styles to use
Serif

Colors
9bcb3c
acd036
cadf82
f78f20
ffc214
f37122
fbed22
fece3e
faa54b

Requirements
Must have
• A literal representation of the brand QELVA (we don't have a logo for it)

```html
<!DOCTYPE html>
<html lang="en">
<head>
<meta charset="utf-8">
<title>QELVA – Natural Soap with Seabuckthorn and Olive Oil</title>
<link rel="stylesheet" href="https://fonts.googleapis.com/css2?family=Cinzel:wght@400;600&family=Dancing+Script:wght@600&family=Quicksand:wght@500&display=swap">
<style>
  :root {
    --kraft: #c9a57b;
    --kraft-light: #d2b089;
    --badge: #544d47;
    --ink: #3f3a36;
    --white: #ffffff;
    --leaf-green: #8dc63f;
  }
  html, body {
    margin: 0;
    padding: 0;
    overflow: hidden;
    background: var(--kraft);
  }
  .box-face {
    position: relative;
    width: 867px;
    height: 1200px;
    overflow: hidden;
    background:
      radial-gradient(ellipse at 30% 20%, var(--kraft-light) 0%, transparent 60%),
      var(--kraft);
  }
  .watercolor-field {
    position: absolute;
    left: 0;
    top: 540px;
    width: 867px;
    height: 660px;
    background:
      radial-gradient(ellipse 260px 190px at 730px 210px, rgba(243,113,34,0.8) 0%, rgba(243,113,34,0) 100%),
      radial-gradient(ellipse 330px 210px at 300px 260px, rgba(247,143,32,0.72) 0%, rgba(247,143,32,0) 100%),
      radial-gradient(ellipse 420px 260px at 180px 490px, rgba(250,165,75,0.85) 0%, rgba(250,165,75,0) 100%),
      radial-gradient(ellipse 380px 240px at 560px 540px, rgba(255,194,20,0.75) 0%, rgba(255,194,20,0) 100%),
      radial-gradient(ellipse 300px 160px at 460px 400px, rgba(254,206,62,0.55) 0%, rgba(254,206,62,0) 100%),
      linear-gradient(to bottom, rgba(247,143,32,0) 0%, rgba(247,143,32,0.35) 45%, rgba(255,194,20,0.6) 100%);
  }
  .brand-badge {
    position: absolute;
    left: 214px;
    top: 77px;
    width: 444px;
    height: 411px;
  }
  .brand-badge svg {
    position: absolute;
    inset: 0;
  }
  .brand-name {
    position: absolute;
    left: 0;
    right: 0;
    top: 138px;
    margin: 0;
    text-align: center;
    font-family: "Cinzel", serif;
    font-weight: 400;
    font-size: 116px;
    line-height: 1;
    letter-spacing: 2px;
    color: var(--white);
  }
  .brand-tagline {
    position: absolute;
    left: 0;
    right: 0;
    top: 263px;
    margin: 0;
    text-align: center;
    font-family: "Quicksand", sans-serif;
    font-weight: 500;
    font-size: 20px;
    line-height: 1;
    color: var(--leaf-green);
  }
  .product-title {
    margin: 0;
    color: var(--ink);
    font-weight: 400;
  }
  .product-title span {
    position: absolute;
    left: 0;
    right: 0;
    text-align: center;
    line-height: 1;
  }
  .product-title .script {
    font-family: "Dancing Script", cursive;
    font-weight: 600;
  }
  .product-title .ingredient {
    font-family: "Cinzel", serif;
    font-weight: 400;
    font-size: 52px;
    letter-spacing: 3px;
  }
  .product-title .lead { top: 614px; font-size: 72px; }
  .product-title .seabuckthorn { top: 714px; }
  .product-title .and { top: 790px; font-size: 66px; }
  .product-title .olive { top: 879px; }
</style>
</head>
<body>
  <main class="box-face">
    <div class="watercolor-field" role="img" aria-label="Orange and yellow watercolour wash with line-drawn seabuckthorn and olive branches"></div>

    <div class="brand-badge">
      <svg width="444" height="411" viewBox="0 0 444 411" aria-hidden="true">
        <path fill="var(--badge)" d="
          M60 30 Q222 -10 384 30
          Q384 60 414 66 Q454 205 414 345
          Q384 351 384 381 Q222 421 60 381
          Q60 351 30 345 Q-10 205 30 66
          Q60 60 60 30 Z"/>
      </svg>
      <h1 class="brand-name">QELVA</h1>
      <p class="brand-tagline">100% Natural Handmade Soap</p>
    </div>

    <h2 class="product-title">
      <span class="script lead">Natural Soap with</span>
      <span class="ingredient seabuckthorn">SEABUCKTHORN</span>
      <span class="script and">and</span>
      <span class="ingredient olive">OLIVE OIL</span>
    </h2>
  </main>
</body>
</html>
```